Redesign wellness clinic website

The project is redesign a wellness clinic http://www.thornleighvitality.example. The new website is to be responsive,clean,bright and a strong call to action which is to book an appointment. The logo will remain the same but the colour scheme on the website should be reflect purple white and green. I want it to be bright and cheerful and the feeling of clarity. The website shouldn't be overloaded with content but more visuals.

Target Market(s)

Anyone that has corporate wellness benefits within the downtown Toronto core. Majority of audience are professional working in Media, Telecommunications and Investments.

Industry/Entity Type

Health And Wellness

Number of Pages Required

5+ page

Font styles to use
Sans Serif

Colors
ffffff
886aae
acd036

Requirements
Must have
• -Strong call to action which is book an appointment like this page https://www.kestrelmotion.example/
• -Services provided icons on the page like https://www.brightpathvitalityhouse.example/
• - Pictures of a good visualizing a fit and healthy life
• - Strong ratings from Quorva, Zintrel, PostMaz, similar to this website http://www.summitbalancehealth.example/our-team-professionals/
• - Bright and clear
Should not have
• -No black and white images (redo our pictures)
• -Dark themes

```html
<!DOCTYPE html>
<html lang="en">
<head>
<meta charset="utf-8">
<title>Thornleigh Vitality Centre</title>
<link rel="stylesheet" href="https://fonts.googleapis.com/css2?family=Open+Sans:wght@400;600;700&family=Raleway:wght@400;500;600;700&display=swap">
<style>
:root{
  --green:#a9c92a;
  --green-dark:#95b31f;
  --purple:#886aae;
  --ink:#1f1f1f;
  --text:#444;
  --muted:#666;
  --line:#e4e4e4;
  --panel:#f3f3f3;
  --white:#ffffff;
}
*{box-sizing:border-box;margin:0;padding:0}
html,body{width:1200px;height:3462px;overflow:hidden}
body{font-family:"Raleway",Arial,sans-serif;color:var(--text);background:var(--white);position:relative}
.wrap{width:1121px;margin:0 auto;position:relative}
/* header */
.site-header{height:104px;display:flex;align-items:center}
.site-header .wrap{display:flex;align-items:center;justify-content:space-between}
.brand{display:flex;align-items:center;gap:12px}
.brand-mark{width:52px;height:52px;border-radius:50%;background:var(--purple)}
.brand-name{font-weight:700;font-size:16px;color:var(--purple);line-height:1.2}
.brand-phone{font-size:12px;color:var(--green);margin-top:3px;font-weight:600}
.main-nav{display:flex;align-items:center;gap:10px;font-size:14px;color:#333}
.main-nav .sep{color:#777}
.main-nav .active{color:var(--green)}
.btn-appoint{margin-left:16px;background:var(--green);color:#fff;font-size:11px;font-weight:700;height:36px;width:95px;display:flex;align-items:center;justify-content:center;gap:6px;text-transform:uppercase}
/* hero */
.hero{height:568px;background:radial-gradient(ellipse at 25% 40%,#c9a58a 0%,#7a5440 35%,#3a2418 70%,#22140d 100%);position:relative;display:flex;flex-direction:column;align-items:center}
.hero-frame{margin-top:235px;width:735px;height:148px;border:3px solid #fff;display:flex;align-items:center;justify-content:center}
.hero-title{font-family:"Open Sans",Arial,sans-serif;font-weight:600;font-size:44px;color:#fff;letter-spacing:1px}
.hero-sub{font-family:"Open Sans",Arial,sans-serif;color:#fff;font-size:26px;text-align:center;line-height:36px;margin-top:4px}
/* section headings */
.section-title{text-align:center;font-weight:700;font-size:28px;color:var(--ink);letter-spacing:.5px}
.ornament{display:block;margin:8px auto 0}
/* services */
.services{padding-top:720px}
.services{padding-top:0;position:absolute;top:720px;left:0;width:1200px}
.service-row{display:flex;gap:30px;margin-top:44px}
.service-card{width:353px;height:480px;background:#fafafa;border:2px solid #eee;text-align:center;padding-top:6px}
.service-card.is-active{border-color:var(--green)}
.service-photo{width:236px;height:236px;border-radius:50%;margin:0 auto}
.service-name{font-size:25px;color:var(--ink);margin:25px 0 8px}
.is-active .service-name{color:var(--green)}
.service-list{list-style:none;font-size:15px;line-height:23px;color:#333}
.btn-more{display:inline-block;width:117px;height:36px;line-height:34px;font-size:12px;border:1px solid #999;color:#333;margin-top:24px;text-transform:uppercase}
.is-active .btn-more{background:var(--green);border-color:var(--green);color:#fff}
.slider-arrow{position:absolute;top:1012px;width:30px;height:46px;background:var(--green);display:flex;align-items:center;justify-content:center}
/* visit band */
.visit-band{position:absolute;top:1334px;left:0;width:1200px;height:254px;background:var(--green);text-align:center;color:#fff;padding-top:52px}
.visit-band p{font-weight:700;font-size:22px;line-height:31px}
.btn-map{display:inline-block;background:#fff;color:#333;width:117px;height:36px;line-height:36px;font-size:17px;margin-top:14px;border-radius:2px}
/* blog */
.blog{position:absolute;top:1634px;left:0;width:1200px}
.blog-row{display:flex;gap:55px;margin-top:40px}
.blog-card{width:533px;height:275px;position:relative}
.blog-date{position:absolute;top:0;right:0;width:65px;height:103px;background:var(--green);color:#fff;text-align:center;font-weight:700;padding-top:10px;line-height:25px}
.blog-date .day{font-size:24px}
.blog-date .mon,.blog-date .yr{font-size:19px}
.blog-caption{position:absolute;left:0;right:0;bottom:0;height:66px;background:rgba(40,40,40,.55);color:#fff;font-size:19px;display:flex;align-items:center;padding-left:22px}
/* testimonials */
.testimonials{position:absolute;top:2040px;left:0;width:1200px;height:448px;background:var(--panel);padding-top:38px}
.quote-box{margin-top:30px;background:#fff;border:1px solid #ddd;height:187px;padding:18px 40px;text-align:center;font-size:15px;line-height:27px;color:#555}
.quote-avatar{width:98px;height:98px;border-radius:50%;margin:-48px auto 0;background:linear-gradient(135deg,#8a96a8,#3d4656);border:3px solid #fff;position:relative}
.quote-name{text-align:center;font-size:16px;color:#333;margin-top:10px}
.dots{display:flex;justify-content:center;gap:8px;margin-top:10px}
.dots span{width:9px;height:9px;border-radius:50%;background:#bbb}
.dots span:first-child{background:#333}
/* about */
.about{position:absolute;top:2488px;left:0;width:1200px;height:489px}
.about .wrap{display:flex;justify-content:space-between;padding-top:57px}
.about-copy{width:535px}
.about-copy h2{font-size:28px;font-weight:700;color:var(--ink);letter-spacing:.3px}
.about-copy p{font-size:16px;line-height:27px;text-align:justify;color:#333;margin-top:18px}
.about-video{width:532px;height:376px;margin-top:0;background:linear-gradient(135deg,#eeeeee,#9a9a9a 55%,#5a5a5a);position:relative;top:0}
.video-bar{position:absolute;left:14px;right:14px;bottom:14px;height:38px;background:rgba(30,30,30,.8);display:flex;align-items:center;padding:0 14px;gap:14px}
.video-track{flex:1;height:6px;background:#777;border-radius:3px}
.video-hd{color:#4cb3e8;font-weight:700;font-size:13px;font-family:"Open Sans",Arial,sans-serif}
/* newsletter */
.newsletter{position:absolute;top:2977px;left:0;width:1200px;height:138px;background:var(--green);color:#fff}
.newsletter .wrap{display:flex;align-items:center;height:100%}
.newsletter-text{font-size:14px;font-weight:600;line-height:19px;margin-left:26px;width:650px}
.newsletter-text .gap{margin-top:8px}
.signup{margin-left:auto;display:flex}
.signup-field{width:255px;height:52px;background:#fff;color:#888;font-size:15px;padding-left:14px;display:flex;align-items:center}
.signup-btn{width:112px;height:52px;background:var(--purple);color:#fff;font-size:18px;display:flex;align-items:center;justify-content:center}
/* footer */
.site-footer{position:absolute;top:3115px;left:0;width:1200px;height:347px;background:var(--panel)}
.footer-cols{position:relative;height:270px}
.footer-contact{position:absolute;left:0;top:28px;width:290px;text-align:center;font-size:14px;line-height:22px;color:#222}
.footer-contact strong{display:block;font-weight:700;margin-top:4px}
.socials{display:flex;justify-content:center;gap:8px;margin-top:10px}
.socials span{width:30px;height:30px;border-radius:50%;background:#222}
.socials span:first-child{background:var(--green)}
.footer-divider{position:absolute;left:361px;top:60px;width:1px;height:200px;background:#ccc}
.footer-col{position:absolute;top:42px;font-size:14px;line-height:27px;color:#222}
.footer-col h3{font-size:14px;font-weight:700;color:#222;margin-bottom:10px;text-transform:uppercase}
.footer-col ul{list-style:none}
.footer-col .active{color:var(--purple)}
.partner{width:95px;margin-bottom:16px}
.copyright{position:absolute;left:51px;right:28px;top:278px;border-top:1px solid #ccc;text-align:center;font-size:14px;color:#222;padding-top:16px}
.copyright span{color:var(--purple)}
</style>
</head>
<body>

<header class="site-header">
  <div class="wrap">
    <div class="brand">
      <span class="brand-mark"></span>
      <div>
        <div class="brand-name">Thornleigh Vitality Centre</div>
        <div class="brand-phone">Call 416-555-0142</div>
      </div>
    </div>
    <nav class="main-nav">
      <span class="active">Home</span><span class="sep">/</span>
      <span>Fees &amp; Services</span><span class="sep">/</span>
      <span>Our Staff</span><span class="sep">/</span>
      <span>News</span><span class="sep">/</span>
      <span>Corporate Wellness</span><span class="sep">/</span>
      <span>Forms</span><span class="sep">/</span>
      <span>Contact</span>
      <span class="btn-appoint">
        <svg width="13" height="13" viewBox="0 0 13 13"><rect x="1" y="2" width="11" height="10" fill="none" stroke="#fff" stroke-width="1.5"/><line x1="1" y1="5" x2="12" y2="5" stroke="#fff" stroke-width="1.5"/></svg>
        Appointment
      </span>
    </nav>
  </div>
</header>

<section class="hero" role="img" aria-label="Relaxing spa scene with warm stones and folded towels">
  <div class="hero-frame"><h1 class="hero-title">THORNLEIGH VITALITY CENTER</h1></div>
  <p class="hero-sub">Many Disciplines,One Philosophy<br>Contact 416-555-0142</p>
</section>

<section class="services">
  <div class="wrap">
    <h2 class="section-title">OUR SERVICES</h2>
    <svg class="ornament" width="80" height="14" viewBox="0 0 80 14"><line x1="0" y1="7" x2="32" y2="7" stroke="#333" stroke-width="2"/><line x1="48" y1="7" x2="80" y2="7" stroke="#333" stroke-width="2"/><rect x="35" y="2" width="10" height="10" transform="rotate(45 40 7)" fill="none" stroke="#333" stroke-width="2"/></svg>
    <div class="service-row">
      <article class="service-card is-active">
        <div class="service-photo" role="img" aria-label="Chiropractor adjusting a patient" style="background:linear-gradient(135deg,#c9d6e8,#5d7aa8 60%,#2f4a78)"></div>
        <h3 class="service-name">Chiropractic</h3>
        <ul class="service-list"><li>Adjustment</li><li>Functional Adjustment</li><li>Custom Orthotics and Bracing</li></ul>
        <span class="btn-more">View More</span>
      </article>
      <article class="service-card">
        <div class="service-photo" role="img" aria-label="Physiotherapist treating a patient's leg" style="background:linear-gradient(135deg,#f2f2f2,#a9c2d8 55%,#6d8aa6)"></div>
        <h3 class="service-name">Physiotherapy</h3>
        <ul class="service-list"><li>Physiotherapy</li><li>Athletic Therapy</li><li>Custom Orthotics and Bracing</li></ul>
        <span class="btn-more">View More</span>
      </article>
      <article class="service-card">
        <div class="service-photo" role="img" aria-label="Woman receiving a relaxing massage" style="background:linear-gradient(135deg,#f6e6da,#e2b596 55%,#b9805e)"></div>
        <h3 class="service-name">Massage Therapy</h3>
        <ul class="service-list"><li>Swedish &amp; Hot Stone Massage</li><li>Sports &amp; Shiatsu Massage</li><li>Pregnancy &amp; Thai Massage</li><li>Foot Reflexology &amp; Infant Massage</li></ul>
        <span class="btn-more">View More</span>
      </article>
    </div>
  </div>
</section>
<span class="slider-arrow" style="left:51px"><svg width="12" height="18" viewBox="0 0 12 18"><polyline points="10,2 3,9 10,16" fill="none" stroke="#fff" stroke-width="3"/></svg></span>
<span class="slider-arrow" style="left:1142px"><svg width="12" height="18" viewBox="0 0 12 18"><polyline points="2,2 9,9 2,16" fill="none" stroke="#fff" stroke-width="3"/></svg></span>

<section class="visit-band">
  <p>Visit our new location</p>
  <p>We are open for business at 7:30 am. Open 7 days a week!</p>
  <p>Ask one of our associates about our Referral Reward Program!</p>
  <span class="btn-map">See Map</span>
</section>

<section class="blog">
  <div class="wrap">
    <h2 class="section-title">LATEST BLOG</h2>
    <svg class="ornament" width="80" height="14" viewBox="0 0 80 14"><line x1="0" y1="7" x2="32" y2="7" stroke="#333" stroke-width="2"/><line x1="48" y1="7" x2="80" y2="7" stroke="#333" stroke-width="2"/><rect x="35" y="2" width="10" height="10" transform="rotate(45 40 7)" fill="none" stroke="#333" stroke-width="2"/></svg>
    <div class="blog-row">
      <article class="blog-card" role="img" aria-label="Smiling woman relaxing after a treatment" style="background:linear-gradient(120deg,#d8b08e,#a0704f 55%,#5b3b28)">
        <div class="blog-date"><div class="day">15</div><div class="mon">Aug</div><div class="yr">2017</div></div>
        <div class="blog-caption">Labour Day Weekend Hours</div>
      </article>
      <article class="blog-card" role="img" aria-label="Woman meditating outdoors in a green field" style="background:linear-gradient(180deg,#cfdde8 0%,#9fb58a 45%,#5f7f3e 100%)">
        <div class="blog-date"><div class="day">5</div><div class="mon">June</div><div class="yr">2017</div></div>
        <div class="blog-caption">Think Well Program</div>
      </article>
    </div>
  </div>
</section>

<section class="testimonials">
  <div class="wrap">
    <h2 class="section-title">TESTIMONIALS</h2>
    <svg class="ornament" width="80" height="14" viewBox="0 0 80 14"><line x1="0" y1="7" x2="32" y2="7" stroke="#333" stroke-width="2"/><line x1="48" y1="7" x2="80" y2="7" stroke="#333" stroke-width="2"/><rect x="35" y="2" width="10" height="10" transform="rotate(45 40 7)" fill="none" stroke="#333" stroke-width="2"/></svg>
    <blockquote class="quote-box">Dear Dr. Keller: I attended your clinic recently and was surprised. I am 68 years old and never before was I received so warmly. I believe that natural medicine is the best medicine for all of us. It has fewer and more benign side effects than those created in labs. Your clinic I dream will be the future of health care. My regret is that most patients are misled by the medical and pharmaceutical powers that be to sway their minds to traditional methods of treating their conditions. I wish all of you well in your endeavors.</blockquote>
    <div class="quote-avatar" role="img" aria-label="Portrait of the client"></div>
    <p class="quote-name">Regards Jack</p>
    <div class="dots"><span></span><span></span><span></span></div>
  </div>
</section>

<section class="about">
  <div class="wrap">
    <div class="about-copy">
      <h2>ABOUT THORNLEIGH VITALITY CENTRE</h2>
      <p>Established in 1989 the Thornleigh Vitality Centre has become one of Canada's leaders in providing quality care and innovative wellness programs for the community. The founder and director Dr. Alden Voss's vision has come to life with over 30 practitioners providing a multitude of different services under one roof. Some of the services include Chiropractic, Physiotherapy, Athletic Therapy, Naturopathy, Massage Therapy, Acupuncture and Personal Training. The Thornleigh Vitality Centre has a complete Pilates studio on its premises. We also offer many wellness seminars free of cost to the public. Our Centre is committed to helping improve and extend the lives of as many people as possible in our community. Come and join our Family and start changing your life today.</p>
    </div>
    <div class="about-video" role="img" aria-label="Video of the clinic director speaking about the centre">
      <div class="video-bar">
        <svg width="14" height="16" viewBox="0 0 14 16"><polygon points="1,1 13,8 1,15" fill="#fff"/></svg>
        <span class="video-track"></span>
        <span class="video-hd">HD</span>
      </div>
    </div>
  </div>
</section>

<section class="newsletter">
  <div class="wrap">
    <svg width="72" height="60" viewBox="0 0 72 60"><rect x="3" y="8" width="60" height="44" fill="none" stroke="#fff" stroke-width="3"/><polyline points="3,8 33,32 63,8" fill="none" stroke="#fff" stroke-width="3"/><line x1="40" y1="40" x2="70" y2="22" stroke="#fff" stroke-width="3"/></svg>
    <div class="newsletter-text">
      <p>Our Centre is committed to helping improve and extend the lives of as many people as possible in our community. Come and join our Family and start changing your life today.</p>
      <p class="gap">Planning a wellness fair? We can help!<br>Contact us at info@thornleighvitality.example for more details.</p>
    </div>
    <div class="signup"><span class="signup-field">Email Addresss</span><span class="signup-btn">SIGN UP</span></div>
  </div>
</section>

<footer class="site-footer">
  <div class="wrap footer-cols">
    <div class="footer-contact">
      <svg width="26" height="34" viewBox="0 0 26 34"><path d="M13 1C6 1 1 6 1 13c0 9 12 20 12 20s12-11 12-20C25 6 20 1 13 1z" fill="none" stroke="#886aae" stroke-width="3"/><circle cx="13" cy="13" r="4" fill="none" stroke="#886aae" stroke-width="3"/></svg>
      <strong>Thornleigh Vitality Centre</strong>
      48 Harrow Lane East, Suite 210 Toronto,<br>Ontario M0A 2C4<br>
      Phone: 416-555-0142 | Fax 416-555-0187<br>
      appointments@thornleighvitality.example
      <div class="socials"><span></span><span></span><span></span><span></span><span></span><span></span></div>
    </div>
    <span class="footer-divider"></span>
    <div class="footer-col" style="left:457px">
      <h3>Navigation</h3>
      <ul style="line-height:27px;margin-top:-4px"><li class="active">Home</li><li>Fees and Services</li><li>Our Staff</li><li>News and Updates</li><li>Corporate Wellness</li><li>Forms</li><li>Contact Us</li></ul>
    </div>
    <div class="footer-col" style="left:683px">
      <h3>Hours of Operation</h3>
      <p style="line-height:30px">Monday - Friday 7:30am - 8pm<br>Saturday 10am - 5pm<br>Sunday 10am - 5pm</p>
    </div>
    <div class="footer-col" style="left:976px">
      <h3>Our Partners</h3>
      <div class="partner" style="height:58px;background:#cfe3ef;border-radius:4px"></div>
      <div class="partner" style="width:80px;height:80px;background:#e88a2e;border-radius:50%"></div>
    </div>
    <p class="copyright">Copyright © 2017 <span>Thornleigh Vitality Centre</span> All rights reserved.</p>
  </div>
</footer>

</body>
</html>
```